Modern Yoga Studio Timetable and Flyer Design

We have a comprehensive class timetable and we are wanting to a clean modern look for our Spring timetable.

We require a double sided flyer with our class timetable included.
We would prefer an A5 size (postcard) or DL (1/3 A4).

We would like the final flyer to have.
Side A : Yoga image, logo

Fennel Stretch Hall
address: 4/71 Wexcombe Lane, Pelharton
website: fennelstretch.com.au
mobile: 0471 296 814

Side B: Clear easy to read timetable with a break down of class types and website.

We would also like to have a copy of the timetable itself as a separate jpg or pdf for use on our website to download.

Thank you.
Yours kindly,
Nell

I have attached a sample of another timetable of which I like the look and feel of, however this is just a guide. I've also attached our 'new' schedule in WORD plus uploaded our last design of the front.
Updates

Target Market(s)

Women aged 30-45

Industry/Entity Type

Health And Wellness

Font styles to use
Other font styles liked:
• Brandon Grotesque, Jenna Sue

Colors
6c459b
33a6d7
ffffff

Requirements
Must have
• A definitive colour to decipher between different class types on our timetable. Where each colour represents a different class type. Colours and layouts similar to our website design, see www.fennelstretch.com.au
Nice to have
• I've included a design of another studio whose timetable design I like. One of our own yoga images instead of a stock image.
Should not have
• No dark gridlines between the cells/boxes in the timetables. Please don't use stock yoga images.

```html
<!DOCTYPE html>
<html lang="en">
<head>
<meta charset="utf-8">
<title>Fennel Stretch Hall – Spring Timetable Flyer</title>
<link href="https://fonts.googleapis.com/css2?family=Josefin+Sans:wght@300;400;600&display=swap" rel="stylesheet">
<style>
  :root {
    --backdrop: #3a3a3c;
    --paper: #f7f7f8;
    --sky: #4a86d4;
    --ink: #333333;
    --brand-blue: #3b7fc4;
    --navy-a: #2c3f95;
    --navy-b: #1e2c72;
    --day-blue: #0f74bf;
    --time-blue: #6fd0f6;
    --empty: #f4f4f6;
    --rise: #f5a08b;
    --vinyasa: #fff69e;
    --slow: #f2b6a6;
    --yin: #b9b9bb;
    --pregnancy: #bfd631;
    --mum: #f9b65b;
    --kids: #f3a7c9;
    --teens: #a9dbe6;
    --flow-restore: #c4d2a1;
    --yin-restore: #9ea2d2;
    --wellness: #fdc88f;
  }
  * { box-sizing: border-box; margin: 0; padding: 0; }
  html, body { width: 918px; height: 1200px; overflow: hidden; }
  body { background: var(--backdrop); font-family: "Josefin Sans", sans-serif; color: var(--ink); position: relative; }

  .card { position: absolute; left: 80px; width: 741px; height: 523px; background: var(--paper); overflow: hidden; }
  .card--front { top: 70px; }
  .card--back { top: 622px; background: #ffffff; }

  /* Front */
  .sky-shape { position: absolute; inset: 0; }
  .ornament { position: absolute; left: 25px; top: 0; width: 375px; height: 140px;
    background: radial-gradient(ellipse at 50% 0%, #c9bfe0 0%, #e4e0ee 55%, rgba(247,247,248,0) 80%); }
  .brand-name { position: absolute; left: 38px; top: 150px; font-size: 27px; font-weight: 400;
    color: var(--brand-blue); letter-spacing: 3px; }
  .studio-photo { position: absolute; left: 0; right: 0; bottom: 0; height: 126px;
    background: linear-gradient(180deg, #b08b5e 0%, #9c7a50 60%, #8a6c46 100%); }
  .contact { position: absolute; left: 30px; top: 232px; width: 185px; text-align: center; }
  .contact__name { font-size: 20px; font-weight: 600; text-align: left; margin-bottom: 14px; letter-spacing: 0.3px; }
  .contact__line { font-size: 13px; line-height: 18px; font-weight: 300; }
  .book-online { position: absolute; left: 580px; top: 256px; width: 113px; height: 30px;
    background: #f1f1f1; border: 1px solid #cfcfcf; font-size: 17px; font-weight: 400;
    display: flex; align-items: center; justify-content: center; letter-spacing: 0.5px; }

  /* Back */
  .timetable-head { position: absolute; left: 0; top: 0; width: 100%; height: 54px;
    background: linear-gradient(90deg, var(--navy-b), var(--navy-a) 50%, var(--navy-b));
    color: #fff; font-size: 24px; letter-spacing: 1.6px; text-align: center; line-height: 58px; font-weight: 400; }
  .timetable { position: absolute; left: 29px; top: 71px; display: grid;
    grid-template-columns: 50px 82px 83px 86px 115px 94px 84px 59px;
    grid-template-rows: 35px repeat(13, 26px);
    column-gap: 4.5px; row-gap: 3.6px; }
  .timetable > div { display: flex; align-items: center; justify-content: center;
    font-size: 10.5px; text-transform: uppercase; white-space: nowrap; padding-top: 2px; }
  .day { background: var(--day-blue); color: #fff; font-size: 13px !important; }
  .corner { background: transparent; }
  .time { background: var(--time-blue); text-transform: none !important; justify-content: flex-start !important; padding-left: 5px; }
  .empty { background: var(--empty); }
  .c-rise { background: var(--rise); }
  .c-vinyasa { background: var(--vinyasa); }
  .c-slow { background: var(--slow); }
  .c-yin { background: var(--yin); }
  .c-pregnancy { background: var(--pregnancy); }
  .c-mum { background: var(--mum); }
  .c-kids { background: var(--kids); }
  .c-teens { background: var(--teens); }
  .c-flow-restore { background: var(--flow-restore); }
  .c-yin-restore { background: var(--yin-restore); }
  .c-wellness { background: var(--wellness); }
  .timetable-foot { position: absolute; left: 0; bottom: 0; width: 100%; height: 22px;
    background: linear-gradient(90deg, #1463b8 0%, #1a7fd0 30%, #12aee8 65%, #0f6fc0 100%); }
  .timetable-foot__note { position: absolute; left: 28px; top: 4px; color: #fff; font-size: 10px; letter-spacing: 0.6px; }
</style>
</head>
<body>

<section class="card card--front">
  <svg class="sky-shape" width="741" height="523" viewBox="0 0 741 523">
    <polygon points="741,0 741,400 290,400" fill="#4a86d4"/>
  </svg>
  <div class="ornament" role="img" aria-label="Decorative mandala ornament in purple and grey"></div>
  <div class="brand-name">Fennel Stretch Hall</div>
  <div class="studio-photo" role="img" aria-label="Studio photo of a woman in downward dog pose on a woven mat"></div>
  <div class="contact">
    <h1 class="contact__name">Fennel Stretch Hall</h1>
    <p class="contact__line">4/71 Wexcombe Lane,</p>
    <p class="contact__line">Pelharton</p>
    <p class="contact__line">Mobile: 0471 296 814</p>
    <p class="contact__line">hello@fennelstretch.com.au</p>
  </div>
  <div class="book-online">book online</div>
</section>

<section class="card card--back">
  <h2 class="timetable-head">FENNEL STRETCH SPRING TIMETABLE</h2>
  <div class="timetable">
    <div class="corner"></div><div class="day">Monday</div><div class="day">Tuesday</div><div class="day">Wednesday</div><div class="day">Thursday</div><div class="day">Friday</div><div class="day">Saturday</div><div class="day">Sunday</div>

    <div class="time">05.45 am</div><div class="empty"></div><div class="c-rise">Rise + Shine*</div><div class="empty"></div><div class="c-rise">Rise + Shine*</div><div class="empty"></div><div class="empty"></div><div class="empty"></div>

    <div class="time">09.00 am</div><div class="empty"></div><div class="empty"></div><div class="empty"></div><div class="empty"></div><div class="empty"></div><div class="c-vinyasa">Vinyasa Flow</div><div class="empty"></div>

    <div class="time">09.15 am</div><div class="empty"></div><div class="c-vinyasa">Vinyasa Flow</div><div class="empty"></div><div class="empty"></div><div class="empty"></div><div class="empty"></div><div class="empty"></div>

    <div class="time">09.30 am</div><div class="c-slow">Slow Flow</div><div class="empty"></div><div class="empty"></div><div class="c-vinyasa">Vinyasa Flow</div><div class="empty"></div><div class="empty"></div><div class="c-yin">Yin</div>

    <div class="time">10.30 am</div><div class="empty"></div><div class="empty"></div><div class="empty"></div><div class="empty"></div><div class="empty"></div><div class="c-pregnancy">Pregnancy*</div><div class="empty"></div>

    <div class="time">11.00 am</div><div class="empty"></div><div class="c-mum">Mum + Baby*</div><div class="empty"></div><div class="c-mum">Mum + Baby*</div><div class="empty"></div><div class="empty"></div><div class="empty"></div>

    <div class="time">12.15 pm</div><div class="empty"></div><div class="empty"></div><div class="empty"></div><div class="c-pregnancy">Pregnancy</div><div class="empty"></div><div class="empty"></div><div class="empty"></div>

    <div class="time">04.00 pm</div><div class="empty"></div><div class="empty"></div><div class="c-kids">Kids 8-12*</div><div class="c-kids">Kids 5- 7*</div><div class="empty"></div><div class="c-vinyasa">Vinyasa Flow</div><div class="empty"></div>

    <div class="time">04.45 pm</div><div class="empty"></div><div class="empty"></div><div class="c-teens">Teens12-16*</div><div class="empty"></div><div class="empty"></div><div class="empty"></div><div class="empty"></div>

    <div class="time">05.00 pm</div><div class="empty"></div><div class="empty"></div><div class="empty"></div><div class="c-teens">Teens 12 – 16*</div><div class="empty"></div><div class="empty"></div><div class="empty"></div>

    <div class="time">06.00 pm</div><div class="c-pregnancy">Pregnancy*</div><div class="c-vinyasa">Vinyasa Flow</div><div class="c-slow">Slow Flow</div><div class="empty"></div><div class="c-flow-restore">Flow + Restore</div><div class="empty"></div><div class="empty"></div>

    <div class="time">06.15 pm</div><div class="empty"></div><div class="empty"></div><div class="empty"></div><div class="c-pregnancy">Pregnancy*</div><div class="empty"></div><div class="empty"></div><div class="empty"></div>

    <div class="time">07.30 pm</div><div class="c-vinyasa">Vinyasa Flow</div><div class="c-pregnancy">Pregnancy*</div><div class="c-yin-restore">Yin + Restore</div><div class="c-wellness">Women’s Wellness*</div><div class="empty"></div><div class="empty"></div><div class="empty"></div>
  </div>
  <div class="timetable-foot">
    <svg width="741" height="22" viewBox="0 0 741 22" style="position:absolute;left:0;top:0">
      <polygon points="150,22 163,0 170,0 157,22" fill="#ffffff"/>
    </svg>
    <span class="timetable-foot__note">* bookings essential</span>
  </div>
</section>

</body>
</html>
```